Soy Candle Business needs a label design

We need a label design for a new company selling soy candles - Velvet Hearth Co.

We are using apothecary jars in 3 sizes.
As per attached candles will be dressed with a beautiful black bow and all finished with a diamante in centre of bow.

We would like label done on lid of candle jars - 5cm circle (5cm from one side to the other), this way one label will fit each product size. Label will be done as a sticker.

We are thinking of the background colour to be black, however are open to recommendations. We want label to be classy, elegant and simple.

Inspiration for candle design came from attached invitation that features the bow, and beautiful vintage paper on top area.

Label should include the following 3 pieces of information:
Velvet Hearth Co (company name)
Coconut Lime (this will change depending on fragrance)
Soy Candle

Velvet Hearth Co does not have a company logo... what is done for the label will set tone for what is done across other elements of business moving forward.

Industry/Entity Type

Business

Requirements
Must have
• Velvet Hearth Co
Fragrance Flavour
Soy Candle

```html
<!DOCTYPE html>
<html lang="en">
<head>
<meta charset="UTF-8">
<title>Velvet Hearth Co — Soy Candle Lid Label</title>
<link rel="stylesheet" href="https://fonts.googleapis.com/css2?family=Great+Vibes&family=Montserrat:wght@600&display=swap">
<style>
  :root {
    --page: #ffffff;
    --label-black: #030303;
    --chain-silver: #8c8c8c;
    --flourish-silver: #6e6e6e;
    --script-silver: #c8c8c8;
    --detail-grey: #a6a6a6;
  }
  html, body {
    margin: 0;
    padding: 0;
    width: 1198px;
    height: 1200px;
    overflow: hidden;
    background: var(--page);
  }
  .label {
    position: relative;
    width: 1198px;
    height: 1200px;
  }
  .label-art {
    position: absolute;
    inset: 0;
    width: 1198px;
    height: 1200px;
  }
  .brand-name {
    position: absolute;
    left: 0;
    right: 78px;
    top: 425px;
    margin: 0;
    text-align: center;
    font-family: "Great Vibes", cursive;
    font-weight: 400;
    font-size: 142px;
    line-height: 1;
    white-space: nowrap;
    color: var(--script-silver);
  }
  .product-details {
    position: absolute;
    left: 0;
    right: 60px;
    top: 670px;
    margin: 0;
    text-align: center;
    font-family: "Montserrat", sans-serif;
    font-weight: 600;
    font-size: 54px;
    line-height: 80px;
    color: var(--detail-grey);
  }
  .product-details span { display: block; }
</style>
</head>
<body>
  <main class="label">
    <svg class="label-art" viewBox="0 0 1198 1200" xmlns="http://www.w3.org/2000/svg">
      <defs>
        <clipPath id="disc-clip">
          <circle cx="599" cy="600" r="597"/>
        </clipPath>
        <radialGradient id="flourish-tone" cx="0.45" cy="0.45" r="0.6">
          <stop offset="0" stop-color="#6e6e6e" stop-opacity="0.5"/>
          <stop offset="1" stop-color="#6e6e6e" stop-opacity="0"/>
        </radialGradient>
      </defs>
      <circle class="label-disc" cx="599" cy="600" r="597" fill="var(--label-black)"/>
      <g clip-path="url(#disc-clip)">
        <circle class="chain-border" cx="599" cy="600" r="555" fill="none"
                stroke="var(--chain-silver)" stroke-opacity="0.45" stroke-width="60"
                role="img" aria-label="Decorative chain-link pattern circling the label edge"/>
        <ellipse class="flourish-area" cx="320" cy="340" rx="290" ry="250"
                 fill="url(#flourish-tone)"
                 role="img" aria-label="Ornamental vintage swirl flourish in the upper left"/>
      </g>
    </svg>
    <h1 class="brand-name">Velvet Hearth Co</h1>
    <p class="product-details">
      <span class="fragrance">Coconut Lime</span>
      <span class="product-type">Soy Candle</span>
    </p>
  </main>
</body>
</html>
```